Thats it....YYYEEAAHHH....Right there...... show me the money!!!

The name of the business is "Maple Ridge Rentals, LLC." Two of our partners are police officers which is where we get the blue line from and we will be purchasing properties to hold and rent or flip. I think it's obvious that if you incorporate the "blue line" that represents police officers and a house, that would be very representative of the name of our business and still portray what we do. So, a house where the outside lines of it are the blue line would be pretty easy.

Target Market(s)

People looking to rent property, military, college students, blue collar working class

Contact Information for Business Card

I think it's obvious that if you incorporate the "blue line" that represents police officers and a house, that would be very representative of the name of our business and still portray what we do. So, a house where the outside lines of it are the blue line would be pretty easy.

Requirements
Must have
• The police "Blue Line" and a house or housing
Nice to have
• something glossy on the front side. We want it to pop but get the point across

```html
<!DOCTYPE html>
<html lang="en">
<head>
<meta charset="utf-8">
<title>Maple Ridge Rentals, LLC — Business Card</title>
<link rel="stylesheet" href="https://fonts.googleapis.com/css2?family=Cinzel:wght@600&family=Tinos&display=swap">
<style>
  :root {
    --page-bg: #e9e6e1;
    --card-black: #050505;
    --card-sheen: #1c1c1f;
    --accent-blue: #3f3d9b;
    --text-white: #f4f4f4;
    --text-soft: #d9d9d9;
    --window-gold: #f2c21b;
  }
  * { margin: 0; padding: 0; box-sizing: border-box; }
  html, body {
    width: 1200px;
    height: 799px;
    overflow: hidden;
    background: var(--page-bg);
  }
  .business-card {
    position: absolute;
    left: 100px;
    top: 113px;
    width: 1000px;
    height: 572px;
    background: linear-gradient(160deg, var(--card-sheen) 0%, var(--card-black) 38%, var(--card-black) 100%);
    border-radius: 6px;
    box-shadow: 0 14px 34px rgba(0,0,0,0.35);
    overflow: hidden;
  }
  .accent-band {
    position: absolute;
    left: 0;
    top: 150px;
    width: 100%;
    height: 104px;
    background: var(--accent-blue);
  }
  .holder {
    position: absolute;
    left: 62px;
    top: 164px;
    color: var(--text-white);
    font-family: "Cinzel", serif;
    font-weight: 600;
  }
  .holder-name {
    font-size: 44px;
    letter-spacing: 1px;
    line-height: 1.1;
  }
  .holder-role {
    font-size: 24px;
    letter-spacing: 1px;
    line-height: 1.2;
  }
  .contact {
    position: absolute;
    left: 70px;
    top: 352px;
    color: var(--text-white);
    font-family: "Tinos", serif;
    font-size: 24px;
    line-height: 1.2;
  }
  .contact-address { margin-bottom: 14px; }
  .contact-row {
    display: flex;
    align-items: center;
    gap: 18px;
    margin-bottom: 6px;
  }
  .contact-row svg { width: 26px; height: 26px; flex: none; }
  .contact-web {
    margin-top: 4px;
    color: var(--text-soft);
  }
  .brand {
    position: absolute;
    left: 600px;
    top: 318px;
    display: flex;
    align-items: center;
    gap: 20px;
    color: var(--text-white);
    font-family: "Cinzel", serif;
    font-weight: 600;
  }
  .brand-square {
    width: 34px;
    height: 34px;
    background: var(--window-gold);
    flex: none;
  }
  .brand-name {
    font-size: 40px;
    line-height: 1.1;
    letter-spacing: 1px;
  }
</style>
</head>
<body>
  <main class="business-card">
    <div class="accent-band"></div>

    <div class="holder">
      <p class="holder-name">Daniel Hart</p>
      <p class="holder-role">Director</p>
    </div>

    <div class="contact">
      <p class="contact-address">118, Cedar Court<br>Linden Avenue, CA 35207</p>
      <p class="contact-row">
        <svg viewBox="0 0 26 26" aria-hidden="true">
          <rect x="6" y="2" width="14" height="22" rx="2" fill="none" stroke="#f4f4f4" stroke-width="2"/>
          <rect x="9" y="5" width="8" height="11" fill="#f4f4f4"/>
          <circle cx="13" cy="20" r="1.5" fill="#f4f4f4"/>
        </svg>
        <span>410 . 555 .0187</span>
      </p>
      <p class="contact-row">
        <svg viewBox="0 0 26 26" aria-hidden="true">
          <rect x="2" y="6" width="22" height="15" fill="none" stroke="#f4f4f4" stroke-width="2"/>
          <path d="M2 6 L13 15 L24 6" fill="none" stroke="#f4f4f4" stroke-width="2"/>
        </svg>
        <span>info@mapleridgerentals.com</span>
      </p>
      <p class="contact-web">www.mapleridgerentals.com</p>
    </div>

    <div class="brand">
      <span class="brand-square"></span>
      <p class="brand-name">Maple Ridge<br>Rentals, LLC</p>
    </div>
  </main>
</body>
</html>
```